Cedar nest sal
Affordable luxury
Professional
Paul dorsey
Doesn't matter, just write anything, will finalize later
Pauldorsey@quillmarsh.net
All I need is a template that suits the logo, I expect a draft template from your side.
It should include, the name, title, company logo, subtitle, website address, physical address, phone number and email. Thank you
Please suggest
Design number 1 will be used
red as second option

```html
<!DOCTYPE html>
<html lang="en">
<head>
<meta charset="utf-8">
<title>Cedar Nest Sal – Business Card</title>
<link href="https://fonts.googleapis.com/css2?family=Crimson+Text:ital,wght@0,400;0,600;1,600;1,700&display=swap" rel="stylesheet">
<style>
  :root {
    --leaf-green: #6a9a2a;
    --leaf-green-dark: #557f1e;
    --bark-brown: #5e3214;
    --card-white: #ffffff;
    --text-grey: #6b6b6b;
    --backdrop: #e4e4e2;
  }
  html, body {
    margin: 0;
    width: 1200px;
    height: 780px;
    overflow: hidden;
    background: var(--backdrop);
    font-family: "Crimson Text", Georgia, serif;
  }
  .business-card {
    position: absolute;
    left: 40px;
    top: 40px;
    width: 1120px;
    height: 700px;
    border-radius: 36px;
    overflow: hidden;
    background: var(--card-white);
    box-shadow: 0 6px 24px rgba(0,0,0,0.18);
  }
  .card-shapes {
    position: absolute;
    inset: 0;
  }
  .holder-name {
    position: absolute;
    right: 64px;
    top: 44px;
    margin: 0;
    font-size: 46px;
    font-weight: 700;
    font-style: italic;
    color: var(--leaf-green);
  }
  .holder-title {
    position: absolute;
    right: 64px;
    top: 100px;
    margin: 0;
    font-size: 30px;
    color: var(--text-grey);
  }
  .brand {
    position: absolute;
    left: 70px;
    top: 330px;
    display: flex;
    align-items: center;
    gap: 18px;
  }
  .brand-mark {
    width: 40px;
    height: 40px;
    background: var(--bark-brown);
  }
  .brand-name {
    font-size: 66px;
    font-weight: 600;
    color: var(--bark-brown);
    letter-spacing: 1px;
  }
  .postal-address {
    position: absolute;
    right: 64px;
    top: 398px;
    margin: 0;
    font-style: normal;
    text-align: right;
    font-size: 28px;
    line-height: 1.25;
    color: var(--card-white);
  }
  .phone-row {
    position: absolute;
    right: 64px;
    top: 498px;
    display: flex;
    gap: 24px;
    font-size: 28px;
    color: var(--card-white);
  }
  .phone-row span, .web-row span {
    display: inline-flex;
    align-items: center;
    gap: 8px;
  }
  .web-row {
    position: absolute;
    left: 300px;
    top: 620px;
    display: flex;
    gap: 34px;
    font-size: 28px;
    color: var(--card-white);
  }
  .icon {
    width: 24px;
    height: 24px;
    fill: var(--card-white);
  }
</style>
</head>
<body>
  <section class="business-card">
    <svg class="card-shapes" viewBox="0 0 1120 700" preserveAspectRatio="none" aria-hidden="true">
      <path d="M0,575 C320,540 720,440 1120,185 L1120,700 L0,700 Z" fill="var(--leaf-green)"/>
      <path d="M0,538 C380,508 780,392 1120,150 L1120,178 C720,432 320,548 0,572 Z" fill="var(--bark-brown)"/>
      <path d="M0,520 C380,492 780,378 1120,128 L1120,150 C780,392 380,508 0,538 Z" fill="var(--card-white)"/>
    </svg>

    <h1 class="holder-name">Paul dorsey</h1>
    <p class="holder-title">job title</p>

    <div class="brand">
      <span class="brand-mark"></span>
      <span class="brand-name">Cedar Nest Sal</span>
    </div>

    <address class="postal-address">
      Suite 102 Street name<br>
      State, Zip 2034,Country
    </address>

    <div class="phone-row">
      <span>
        <svg class="icon" viewBox="0 0 24 24"><path d="M6.6 10.8a15.1 15.1 0 0 0 6.6 6.6l2.2-2.2a1 1 0 0 1 1-.25 11.4 11.4 0 0 0 3.6.57 1 1 0 0 1 1 1V20a1 1 0 0 1-1 1A17 17 0 0 1 3 4a1 1 0 0 1 1-1h3.5a1 1 0 0 1 1 1c0 1.25.2 2.45.57 3.57a1 1 0 0 1-.25 1z"/></svg>
        127 555 0184
      </span>
      <span>
        <svg class="icon" viewBox="0 0 24 24"><path d="M4 9h16v11H4z M7 3h10v5H7z M7 13h3v2H7zm4 0h3v2h-3zm4 0h2v2h-2zM7 16h3v2H7zm4 0h3v2h-3z"/></svg>
        345 555 0172
      </span>
    </div>

    <div class="web-row">
      <span>
        <svg class="icon" viewBox="0 0 24 24"><path d="M12 2a10 10 0 1 0 5 18.7l-1-1.7A8 8 0 1 1 20 12v1.2a1.8 1.8 0 0 1-3.6 0V7.5h-2v.9A5 5 0 1 0 15 16a3.8 3.8 0 0 0 7-2.8V12A10 10 0 0 0 12 2zm0 13a3 3 0 1 1 0-6 3 3 0 0 1 0 6z"/></svg>
        Pauldorsey@quillmarsh.net
      </span>
      <span>
        <svg class="icon" viewBox="0 0 24 24"><path d="M12 2a10 10 0 1 0 0 20 10 10 0 0 0 0-20zm6.9 6h-3a15 15 0 0 0-1.3-3.9A8 8 0 0 1 18.9 8zM12 4a13 13 0 0 1 1.9 4h-3.8A13 13 0 0 1 12 4zM4.3 14a8 8 0 0 1 0-4h3.3a16 16 0 0 0 0 4zm.8 2h3a15 15 0 0 0 1.3 3.9A8 8 0 0 1 5.1 16zm3-8h-3a8 8 0 0 1 4.3-3.9A15 15 0 0 0 8.1 8zM12 20a13 13 0 0 1-1.9-4h3.8A13 13 0 0 1 12 20zm2.3-6H9.7a14 14 0 0 1 0-4h4.6a14 14 0 0 1 0 4zm.3 5.9a15 15 0 0 0 1.3-3.9h3a8 8 0 0 1-4.3 3.9zm1.8-5.9a16 16 0 0 0 0-4h3.3a8 8 0 0 1 0 4z"/></svg>
        www.cedarnestsal.net
      </span>
    </div>
  </section>
</body>
</html>
```